Nolvik Imaging Center web design and code

We need a new website for a Diagnostic Imaging Center in Fort Lauderdale, Florida.
The center has new RO advanced diagnostic equipment including a 3.0 Tesla MRI, a 128 slice PET/CT and a Varen T4 Ultrasound. Our facility has just been renovated and we have a lot of images, both facility and modality to use.
We have two client types, doctors who send their patients to our clinical Nolvik Center division, and clients who self-refer for screening studies to our Wellspire division. Both logos are attached. Please use the colors in the logos for the layout. Site should be coded in conventional HTML with CSS, but support multiple devices.
Updates

Reason: Waiting for additional designs. Most of the current designs are very similar in their structure and we would like more variety in terms of layout.

Target Market(s)

Doctors who refer patients for MRI, CT, PET, Bone Density and Ultrasound scans,
and
Retail clients who want full-body screening using MRI.

Industry/Entity Type

Medical Imaging

Coding

Coded - Design and coding required

Number of Pages Required

5+ page

Font styles to use
Sans Serif
Other font styles liked:
• Arquitecta

Requirements
Must have
• A good balance between color, shape, message and people/machine images.
• Must have images of the various machines, (RO Quillmark TN480, RO Quillmark 370, RO Varen T4) happy patients, clinical people, facility images and information about scans, preparations, costs, insurances we take.
• Must have links for social media and dynamic imagery.
Nice to have
• Some interactivity would be nice, including contact forms and scheduling application, Location map, directions, downloadable forms, history.
Should not have
• We do not want this to be built on WordPress platform. Should not be bound to a database platform that is proprietary or difficult to move.

```html
<!DOCTYPE html>
<html lang="en">
<head>
<meta charset="utf-8">
<title>Nolvik Imaging Center</title>
<link href="https://fonts.googleapis.com/css2?family=Open+Sans:wght@400;600;700&family=Roboto+Condensed:wght@400;700&display=swap" rel="stylesheet">
<style>
:root{
  --green:#8cc63f;
  --green-dark:#76ad2c;
  --ink:#333a40;
  --text:#6b7177;
  --muted:#9aa0a5;
  --dark:#2c3035;
  --darker:#23262a;
  --light:#f1f2f3;
  --line:#e2e4e6;
  --white:#ffffff;
}
*{margin:0;padding:0;box-sizing:border-box}
html,body{width:1200px;height:3980px;overflow:hidden}
body{position:relative;background:var(--white);font-family:"Open Sans",Arial,sans-serif;color:var(--text);font-size:13px;line-height:1.55}
.abs{position:absolute}
.btn{display:inline-block;background:var(--green);color:var(--white);font-weight:700;font-size:11px;letter-spacing:.5px;text-transform:uppercase;border-radius:20px;padding:9px 26px;text-align:center}
.photo{position:absolute}
h2.section-title{position:absolute;left:0;width:1200px;text-align:center;font-family:"Roboto Condensed",Arial,sans-serif;font-weight:400;font-size:34px;color:var(--ink)}

/* header */
.site-header{left:0;top:0;width:1200px;height:90px;background:var(--white)}
.brand{left:88px;top:20px;display:flex;align-items:center;gap:12px}
.brand-dot{width:44px;height:44px;border-radius:50%;background:var(--green)}
.brand-name{font-family:"Roboto Condensed",Arial,sans-serif;font-weight:700;font-size:22px;line-height:1.05;color:var(--ink);width:190px}
.main-nav{right:100px;top:30px;display:flex;align-items:center;gap:34px;font-size:11px;font-weight:700;color:var(--ink);letter-spacing:.5px}
.main-nav .active{color:var(--green)}
.search-btn{width:32px;height:32px;border-radius:50%;background:var(--green);display:flex;align-items:center;justify-content:center}

.hero{left:0;top:90px;width:1200px;height:420px;background:linear-gradient(100deg,#9fb4c3 0%,#d9e2e8 40%,#b8c7d2 70%,#8ea3b2 100%)}
.hero-caption{left:88px;top:350px;width:260px;padding:18px 20px;background:rgba(35,40,45,.82);border-left:4px solid var(--green)}
.hero-caption h1{font-family:"Roboto Condensed",Arial,sans-serif;font-size:26px;line-height:1.15;color:var(--white);font-weight:700;text-transform:uppercase}
.hero-arrows{display:flex;gap:6px;margin-top:12px}
.hero-arrows span{width:26px;height:26px;background:var(--green);display:flex;align-items:center;justify-content:center}
.slider-dots{left:0;top:518px;width:1200px;display:flex;justify-content:center;gap:8px}
.slider-dots span{width:10px;height:10px;border-radius:50%;border:1px solid var(--muted)}
.slider-dots span.on{background:var(--green);border-color:var(--green)}

/* welcome */
.welcome{left:0;top:548px;width:1200px;height:112px;background:var(--light)}
.welcome h2{position:absolute;left:100px;top:38px;font-family:"Roboto Condensed",Arial,sans-serif;font-weight:400;font-size:30px;color:var(--ink)}
.welcome .btn{position:absolute;right:100px;top:38px;width:170px}

/* why */
.why-text{left:96px;top:722px;width:230px}
.why-text h2{font-family:"Roboto Condensed",Arial,sans-serif;font-weight:400;font-size:36px;line-height:1.1;color:var(--ink)}
.why-text p{margin:50px 0 24px;font-size:11px;color:var(--green-dark);line-height:1.6}
.why-photo{left:330px;top:720px;width:350px;height:330px;background:linear-gradient(135deg,#e9eef1,#c6d4dd 60%,#9fb6c4)}
.accordion{left:700px;top:720px;width:400px}
.acc-open{background:var(--green);color:var(--white);padding:18px 20px;height:160px}
.acc-open h3{font-size:16px;font-weight:600;margin-bottom:8px}
.acc-open p{font-size:11px;line-height:1.6;margin-bottom:10px}
.acc-open .more{font-size:11px;font-weight:700}
.acc-item{margin-top:14px;background:var(--light);padding:18px 20px;font-size:15px;color:var(--ink)}

/* who */
.who{left:0;top:1112px;width:1200px;height:336px;background:var(--dark)}
.who-text{left:120px;top:1150px;width:380px;text-align:center;color:#c3c7cb}
.who-text .kicker{font-size:9px;letter-spacing:1px;font-weight:700;color:var(--white)}
.who-text h2{font-family:"Roboto Condensed",Arial,sans-serif;font-size:26px;color:var(--white);font-weight:700;margin:6px 0 22px}
.who-text p{font-size:11px;text-align:left;margin-bottom:18px}
.who-photo{left:600px;top:1112px;width:600px;height:336px;background:linear-gradient(90deg,#8b7a6b 0%,#b9a796 35%,#4c6d8c 70%,#2a4968 100%)}

/* services */
.services-cards{left:100px;top:1580px;width:1000px;display:flex;gap:40px}
.card{flex:1;height:290px;background:var(--light);padding:20px}
.card .num{display:inline-block;background:var(--green);color:var(--white);font-size:11px;font-weight:700;padding:2px 10px;margin-bottom:12px}
.card h3{font-family:"Roboto Condensed",Arial,sans-serif;font-weight:700;font-size:24px;line-height:1.15;color:var(--green-dark);margin-bottom:16px}
.card p{font-size:11px}
.card.featured{background:var(--green);color:var(--white);box-shadow:0 6px 14px rgba(0,0,0,.12)}
.card.featured h3{color:var(--white)}
.card.featured .num{background:var(--white);color:var(--green)}

/* updates */
.update-photo{left:100px;top:1950px;width:650px;height:300px;background:linear-gradient(120deg,#5c6f80,#a9b8c3 50%,#6b8496)}
.tag{position:absolute;background:var(--green);color:var(--white);font-size:9px;font-weight:700;padding:4px 10px;letter-spacing:.5px}
.testimonial{left:760px;top:1950px;width:340px;height:300px;background:var(--light);padding:18px 20px}
.testimonial h3{margin-top:38px;font-family:"Roboto Condensed",Arial,sans-serif;font-weight:700;font-size:24px;line-height:1.15;color:var(--ink)}
.t-dots{position:absolute;right:20px;top:22px;display:flex;gap:6px}
.t-dots span{width:9px;height:9px;border-radius:50%;background:#c8ccd0}
.t-dots span.on{background:var(--green)}
.author{display:flex;align-items:center;gap:12px;margin-top:26px}
.author .avatar{width:42px;height:42px;border-radius:50%;background:#b5bec5}
.author b{display:block;font-size:12px;color:var(--ink)}
.author small{font-size:10px;color:var(--muted)}

/* booking */
.booking{left:0;top:2332px;width:1200px;height:430px;background:linear-gradient(90deg,#3b4147 0%,#4f575e 35%,#2e3236 55%,#2c3035 100%)}
.booking-title{left:100px;top:2530px;font-family:"Roboto Condensed",Arial,sans-serif;font-size:50px;line-height:1.02;color:var(--white)}
.booking-title span{color:var(--green)}
.booking-title i{display:block;width:60px;height:3px;background:var(--green);margin-top:20px}
.booking-form{left:600px;top:2362px;width:500px;color:#c9ccd0}
.tabs{display:flex;gap:14px;margin-bottom:26px}
.tabs span{padding:8px 18px;border-radius:20px;font-size:10px;font-weight:700;border:1px solid var(--white);color:var(--white)}
.tabs span.done{background:var(--green);border-color:var(--green)}
.booking-form p{font-size:11px;margin-bottom:20px}
.q-grid{display:grid;grid-template-columns:1fr 1fr;gap:8px 30px;font-size:10px}
.q-grid h4{font-size:10px;font-weight:600;color:var(--white);margin-bottom:6px}
.opt{display:flex;align-items:center;gap:8px;margin-bottom:8px}
.opt i{width:10px;height:10px;border-radius:50%;border:1px solid #c9ccd0}
.booking-form .btn{margin-top:18px}

/* gallery */
.gallery-intro{left:300px;top:2840px;width:600px;text-align:center;font-size:11px}
.gallery-grid{left:88px;top:2940px;width:1012px;display:grid;grid-template-columns:repeat(4,1fr);gap:4px}
.gallery-grid div{height:198px}
.g1{background:linear-gradient(135deg,#d5dde3,#9fb0bd)}
.g2{background:linear-gradient(135deg,#6d8aa3,#c8d5de)}
.g3{background:linear-gradient(135deg,#e1e6ea,#aebdc8)}
.g4{background:linear-gradient(135deg,#bfcbd4,#f0f3f5)}
.gallery-grid .g-hover{background:var(--green);display:flex;flex-direction:column;align-items:center;justify-content:center;color:var(--white);font-size:12px;gap:4px}
.gallery-grid .g-hover small{font-size:9px}
.gallery-more{left:0;top:3414px;width:1200px;text-align:center}

/* footer */
.site-footer{left:0;top:3500px;width:1200px;height:440px;background:var(--dark)}
.footer-cols{left:100px;top:3540px;width:1000px;display:grid;grid-template-columns:1fr 1fr 1.1fr 1fr;gap:30px;color:#9ca2a8;font-size:10px}
.footer-cols h4{font-family:"Roboto Condensed",Arial,sans-serif;font-size:20px;color:var(--white);font-weight:700;margin-bottom:22px}
.footer-cols p{margin-bottom:8px;line-height:1.6}
.footer-cols ul{list-style:none}
.footer-cols li{padding:5px 0;border-bottom:1px solid #3c4147}
.field{height:28px;border:1px solid #464c52;background:#262a2e;margin-bottom:8px;padding:6px 10px;font-size:10px;color:#7d848a}
.field.tall{height:70px}
.footer-cols .btn{float:right}
.copyright{left:0;top:3940px;width:1200px;height:40px;background:var(--darker);color:#868c92;font-size:10px;padding:13px 100px}
</style>
</head>
<body>

<header class="abs site-header">
  <div class="abs brand"><span class="brand-dot"></span><span class="brand-name">Nolvik Imaging Center</span></div>
  <nav class="abs main-nav">
    <span class="active">HOME</span><span>ABOUT US</span><span>SERVICES</span><span>DOWNLOAD</span><span>GALLERY</span><span>CONTACT</span>
    <span class="search-btn"><svg width="14" height="14" viewBox="0 0 14 14"><circle cx="6" cy="6" r="4.2" fill="none" stroke="#fff" stroke-width="1.8"/><line x1="9" y1="9" x2="13" y2="13" stroke="#fff" stroke-width="1.8"/></svg></span>
  </nav>
</header>

<div class="photo hero" role="img" aria-label="Clinicians reviewing MRI scans on monitors in the control room"></div>
<div class="abs hero-caption">
  <h1>Lorem Ipsum Is Simply A Dummy Text</h1>
  <div class="hero-arrows">
    <span><svg width="10" height="10" viewBox="0 0 10 10"><path d="M7 1L3 5l4 4" stroke="#fff" stroke-width="2" fill="none"/></svg></span>
    <span><svg width="10" height="10" viewBox="0 0 10 10"><path d="M3 1l4 4-4 4" stroke="#fff" stroke-width="2" fill="none"/></svg></span>
  </div>
</div>
<div class="abs slider-dots"><span></span><span class="on"></span><span></span></div>

<section class="abs welcome">
  <h2>Welcome To Nolvik Imaging Center</h2>
  <span class="btn">Download</span>
</section>

<section>
  <div class="abs why-text">
    <h2>Why<br>MRI Scan</h2>
    <p>Lorem ipsum dolor sit amet, consectetur adipiscing elit, sed do eiusmod tempor incididunt ut labore et dolore magna aliqua ut enim ad minim veniam.</p>
    <span class="btn">Explore</span>
  </div>
  <div class="photo why-photo" role="img" aria-label="Technician preparing a patient on the MRI scanner table"></div>
  <div class="abs accordion">
    <div class="acc-open">
      <h3>Lorem Ipsum Is Dummy Text</h3>
      <p>Lorem ipsum dolor sit amet, consectetur adipiscing elit, sed do eiusmod tempor incididunt ut labore et dolore magna aliqua. Ut enim ad minim veniam.</p>
      <span class="more">READ MORE</span>
    </div>
    <div class="acc-item">Lorem Ipsum Is Dummy Text</div>
    <div class="acc-item">Lorem Ipsum Dummy Text</div>
  </div>
</section>

<section>
  <div class="abs who"></div>
  <div class="abs who-text">
    <div class="kicker">A FEW OF OUR HISTORY</div>
    <h2>Who We Are &amp; What We Do</h2>
    <p>Lorem Ipsum is simply dummy text of the printing and typesetting industry. Lorem Ipsum has been the industry's standard dummy text ever since the 1500s, when an unknown printer took a galley of type and scrambled it to make a type specimen book.</p>
    <span class="btn">Read More</span>
  </div>
  <div class="photo who-photo" role="img" aria-label="Radiologist in front of screens showing brain scan images"></div>
</section>

<section>
  <h2 class="section-title" style="top:1496px">Our Services</h2>
  <div class="abs services-cards">
    <div class="card"><span class="num">01</span><h3>Lorem Ipsum Is Simply A Dummy Text</h3><p>Lorem ipsum dolor sit amet, consectetur adipiscing elit, sed do eiusmod tempor incididunt ut labore et dolore magna aliqua. Ut enim ad minim veniam.</p></div>
    <div class="card featured"><span class="num">02</span><h3>Lorem Ipsum Is Simply A Dummy Text</h3><p>Lorem ipsum dolor sit amet, consectetur adipiscing elit, sed do eiusmod tempor incididunt ut labore et dolore magna aliqua. Ut enim ad minim veniam.</p></div>
    <div class="card"><span class="num">03</span><h3>Lorem Ipsum Is Simply A Dummy Text</h3><p>Lorem ipsum dolor sit amet, consectetur adipiscing elit, sed do eiusmod tempor incididunt ut labore et dolore magna aliqua. Ut enim ad minim veniam.</p></div>
  </div>
</section>

<section>
  <div class="photo update-photo" role="img" aria-label="Medical team positioning a patient for a CT scan"></div>
  <span class="tag" style="left:112px;top:1962px">LATEST UPDATES</span>
  <div class="abs testimonial">
    <span class="tag" style="left:20px;top:18px">TESTIMONIAL</span>
    <div class="t-dots"><span class="on"></span><span></span><span></span></div>
    <h3>Lorem Ipsum Is Simply A Dummy Text</h3>
    <div class="author"><span class="avatar"></span><div><b>DALE MARSH</b><small>Patient</small></div></div>
  </div>
</section>

<section>
  <div class="photo booking" role="img" aria-label="Smiling patient speaking on the phone to book an appointment"></div>
  <div class="abs booking-title">BOOK AN<br><span>APPOINTMENT</span><br>ONLINE<i></i></div>
  <div class="abs booking-form">
    <div class="tabs"><span class="done">Your Referral</span><span class="done">Your Appointment</span><span>Your Details</span></div>
    <p>Before you can make an appointment, you need to have a completed referral form and a valid photo ID. Please select the options below so your appointment can be arranged through the right team.</p>
    <div class="q-grid">
      <div><h4>Do you have a completed referral form?</h4><div class="opt"><i></i>Yes</div><div class="opt"><i></i>No</div></div>
      <div><h4>How will the scan be funded?</h4><div class="opt"><i></i>Private Medical Insurance</div><div class="opt"><i></i>Self Paying</div><div class="opt"><i></i>Other</div></div>
    </div>
    <span class="btn">Next Step</span>
  </div>
</section>

<section>
  <h2 class="section-title" style="top:2786px">Our Gallery</h2>
  <p class="abs gallery-intro">Lorem Ipsum is simply dummy text of the printing and typesetting industry. Lorem Ipsum has been the industry's standard dummy text ever since the 1500s, when an unknown printer took a galley of type and scrambled it to make a type specimen book.</p>
  <div class="abs gallery-grid">
    <div class="g1" role="img" aria-label="Clinicians with a patient"></div>
    <div class="g2" role="img" aria-label="Doctor reviewing scan images"></div>
    <div class="g-hover"><svg width="34" height="34" viewBox="0 0 34 34"><path d="M17 2v30M2 17h30" stroke="#fff" stroke-width="2"/></svg>Lorem Ipsum<small>Dummy Text</small></div>
    <div class="g3" role="img" aria-label="MRI scanner room"></div>
    <div class="g4" role="img" aria-label="Scanner bore and patient table"></div>
    <div class="g1" role="img" aria-label="Patient on scanner table"></div>
    <div class="g2" role="img" aria-label="Radiographer at the scanner"></div>
    <div class="g3" role="img" aria-label="Patient entering the MRI scanner"></div>
  </div>
  <div class="abs gallery-more"><span class="btn">View More</span></div>
</section>

<footer>
  <div class="abs site-footer"></div>
  <div class="abs footer-cols">
    <div>
      <h4>Contact</h4>
      <p>nolvikimaging.com</p>
      <p>Nolvik Office | Main Office<br>2140 Harbor Crest Blvd, Suite 300<br>Nolvik, FL 33304</p>
      <p>Phone: (954) 555-0187</p>
      <p>Clinic Office<br>880 Seabright Avenue<br>Nolvik, FL 33305<br>hello@nolvikimaging.com</p>
    </div>
    <div>
      <h4>Quick Links</h4>
      <ul><li>Lorem ipsum dolor sit</li><li>Donec nisi lectus</li><li>Praesent vel orci</li><li>Curabitur tincidunt leo</li><li>Aliquam eget nisl nec</li><li>Cras tempor nunc</li><li>Sed mollis justo</li></ul>
    </div>
    <div>
      <h4>Latest Tweets</h4>
      <p>@nolvikimaging Lorem ipsum dolor sit amet, consectetur adipiscing elit sed do eiusmod tempor. 1 day ago</p>
      <p>@nolvikimaging Ut enim ad minim veniam quis nostrud exercitation ullamco laboris nisi. 1 day ago</p>
      <p>@nolvikimaging Duis aute irure dolor in reprehenderit in voluptate velit esse. 2 days ago</p>
    </div>
    <div>
      <h4>Contact Us</h4>
      <div class="field">Full Name</div>
      <div class="field">Email Address</div>
      <div class="field">Subject</div>
      <div class="field tall">Message</div>
      <span class="btn">Submit</span>
    </div>
  </div>
  <div class="abs copyright">Copyright © 2015 nolvikimaging.com | All Rights Reserved</div>
</footer>

</body>
</html>
```